I need this design by August 8th or 9th!
Looking for a classy, but FUn door hangers for a community outreach "Harvest Fun Jamboree." While we are a faith-based organization, we do NOT want this to look religious. I put the LP square blue so you would have a color reference. With grey and orange as an accent color.
Event: Harvest Fun Jamboree!
Location: Calloway Meadow Estates neighborhood pavilion by the red silo.
Date: Friday, August 17th
Time: 5:30 p.m. to 8:30 p.m.
Free food, while supplies last!
Yummy desserts,
Bounce house,
Raffle,
Games and activities.

Target Market(s)

Families in the neighborhood

Colors
acd136
959595
fbee3d

Requirements
Must have
• Door hanger,

```html
<!DOCTYPE html>
<html lang="en">
<head>
<meta charset="utf-8">
<title>Harvest Fun Jamboree Door Hanger</title>
<link href="https://fonts.googleapis.com/css2?family=Oswald:wght@700&family=Lato:wght@400;700&family=Montserrat:wght@800&family=Caveat:wght@500&display=swap" rel="stylesheet">
<style>
  :root {
    --backdrop: #7f7f7f;
    --green-dark: #17753a;
    --green: #25924d;
    --green-light: #2c9e58;
    --doodle: rgba(190, 240, 200, 0.22);
    --white: #ffffff;
    --ink: #1c1c1c;
    --orange: #e5481b;
    --blue: #4a7a9b;
    --blue-shadow: #2f5570;
    --orange-shadow: #a8300e;
    --pencil-yellow: #f2d33a;
    --pencil-green: #8cc63f;
    --pencil-red: #d9342b;
    --ruler: #f1e861;
    --book-red: #b52a2a;
    --book-blue: #2d4f9e;
    --book-yellow: #f2b630;
    --notebook: #3a9a45;
    --calculator: #2c5c99;
    --protractor: #eef2f2;
  }
  * { margin: 0; padding: 0; box-sizing: border-box; }
  html, body { width: 1200px; height: 1200px; overflow: hidden; background: var(--backdrop); }
  .stage { position: relative; width: 1200px; height: 1200px; }

  .hanger {
    position: absolute; left: 382px; top: 82px; width: 436px; height: 1036px;
    overflow: hidden;
    box-shadow: 0 4px 14px rgba(0,0,0,0.35);
  }
  .hanger-bg { position: absolute; inset: 0; }
  .doodle-strip {
    position: absolute; left: 0; top: 0; width: 140px; height: 1036px;
    background: linear-gradient(90deg, var(--doodle), rgba(190,240,200,0));
  }
  .doodle-corner {
    position: absolute; left: 0; top: 0; width: 200px; height: 130px;
    background: radial-gradient(ellipse at 20% 20%, var(--doodle), rgba(190,240,200,0) 70%);
  }

  .supply { position: absolute; border-radius: 6px; }
  .supply.protractor { left: 150px; top: 262px; width: 190px; height: 95px; border-radius: 95px 95px 0 0; background: var(--protractor); transform: rotate(18deg); }
  .supply.pencils { left: 318px; top: 260px; width: 130px; height: 200px; border-radius: 10px;
    background: linear-gradient(160deg, var(--pencil-yellow) 0 25%, var(--pencil-green) 25% 50%, var(--pencil-red) 50% 75%, var(--blue) 75%); transform: rotate(-12deg); }
  .supply.ruler { left: 250px; top: 640px; width: 200px; height: 60px; background: var(--ruler); transform: rotate(-35deg); }
  .supply.notebook { left: 0; top: 565px; width: 120px; height: 140px; background: linear-gradient(135deg, var(--book-blue) 0 30%, var(--notebook) 30%); transform: rotate(-15deg); }
  .supply.books { left: 42px; top: 650px; width: 125px; height: 118px;
    background: linear-gradient(180deg, var(--book-red) 0 28%, #f3ead8 28% 36%, var(--book-blue) 36% 54%, #f3ead8 54% 62%, var(--blue) 62% 78%, var(--book-yellow) 78%); }
  .supply.calculator { left: 308px; top: 662px; width: 66px; height: 80px; background: var(--calculator); transform: rotate(15deg); }

  .badge {
    position: absolute; left: 20px; top: 310px; width: 408px; height: 408px;
    border-radius: 50%; background: var(--white);
  }
  .badge-text {
    position: absolute; left: 20px; top: 310px; width: 408px; height: 408px;
    transform: rotate(-18deg);
    display: flex; flex-direction: column; align-items: center; justify-content: center;
    text-align: center;
  }
  .tagline { font-family: 'Caveat', cursive; font-size: 42px; color: var(--ink); line-height: 1; margin-bottom: 8px; }
  .title { font-family: 'Oswald', sans-serif; font-weight: 700; text-transform: uppercase; line-height: 0.95; letter-spacing: -1px; }
  .title .line-1 { display: block; font-size: 58px; color: var(--orange); text-shadow: 3px 3px 0 var(--orange-shadow); }
  .title .line-2 { display: block; font-size: 60px; color: var(--blue); text-shadow: 3px 3px 0 var(--blue-shadow); }
  .event-date { font-family: 'Lato', sans-serif; font-weight: 700; font-size: 23px; color: var(--orange); margin-top: 12px; }
  .event-time { font-family: 'Lato', sans-serif; font-weight: 400; font-size: 19px; color: var(--blue); margin-top: 2px; }

  .details {
    position: absolute; left: 168px; width: 280px; top: 772px;
    color: var(--white); text-align: center; font-family: 'Lato', sans-serif;
  }
  .pin { display: block; margin: 0 auto 4px; }
  .location { font-size: 18px; line-height: 22px; }
  .free-food { font-family: 'Montserrat', sans-serif; font-weight: 800; font-size: 32px; letter-spacing: 1px; margin-top: 16px; line-height: 1; }
  .supplies-note { font-weight: 700; font-size: 15px; margin-top: 10px; }
  .activities { list-style: none; font-size: 13px; line-height: 16px; margin-top: 14px; }

  .hole-cover { position: absolute; left: 0; top: 0; }
</style>
</head>
<body>
<main class="stage">
  <section class="hanger">
    <svg class="hanger-bg" width="436" height="1036" aria-hidden="true">
      <defs>
        <linearGradient id="board" x1="0" y1="0" x2="0" y2="1">
          <stop offset="0" stop-color="#17753a"/>
          <stop offset="0.45" stop-color="#25924d"/>
          <stop offset="1" stop-color="#1f8644"/>
        </linearGradient>
      </defs>
      <rect width="436" height="1036" fill="url(#board)"/>
    </svg>

    <div class="doodle-strip" role="img" aria-label="Chalk doodles of school supplies, letters and an apple"></div>
    <div class="doodle-corner" role="img" aria-label="Chalk doodle of a basket"></div>

    <div class="supply protractor" role="img" aria-label="Protractor illustration"></div>
    <div class="supply pencils" role="img" aria-label="Coloured pencils illustration"></div>
    <div class="supply ruler" role="img" aria-label="Yellow ruler illustration"></div>
    <div class="supply notebook" role="img" aria-label="Spiral notebooks illustration"></div>

    <div class="badge"></div>
    <div class="badge-text">
      <p class="tagline">#ForMeadowbrook</p>
      <h1 class="title"><span class="line-1">Harvest Fun</span><span class="line-2">Jamboree!</span></h1>
      <p class="event-date">Friday, August 17th</p>
      <p class="event-time">5:30 p.m. to 8:30 p.m</p>
    </div>

    <div class="supply books" role="img" aria-label="Stack of books illustration"></div>
    <div class="supply calculator" role="img" aria-label="Calculator illustration"></div>

    <div class="details">
      <svg class="pin" width="20" height="28" viewBox="0 0 20 28" aria-hidden="true">
        <path d="M10 1a8 8 0 0 0-8 8c0 6 8 15 8 15s8-9 8-15a8 8 0 0 0-8-8z" fill="none" stroke="#fff" stroke-width="2.2"/>
        <circle cx="10" cy="9" r="3" fill="#fff"/>
        <line x1="4" y1="26.5" x2="16" y2="26.5" stroke="#fff" stroke-width="2"/>
      </svg>
      <p class="location">Calloway Meadow<br>Estates neighborhood<br>pavilion by the red silo</p>
      <p class="free-food">FREE FOOD</p>
      <p class="supplies-note">While supplies last!</p>
      <ul class="activities">
        <li>Yummy desserts</li>
        <li>Bounce house</li>
        <li>Raffle</li>
        <li>Games and activities</li>
      </ul>
    </div>

    <svg class="hole-cover" width="436" height="1036" aria-hidden="true">
      <polygon points="106,0 145,0 225,130 190,150" fill="var(--backdrop)"/>
      <circle cx="216" cy="162" r="94" fill="var(--backdrop)"/>
    </svg>
  </section>
</main>
</body>
</html>
```